Haulage company, lets use ruby red white and some 3rd color for web design. and Alder Croft Transport logo

Target Market(s)

Transport industry

Industry/Entity Type

transport

Number of Pages Required

2 page

Requirements
Must have
• Logo

```html
<!DOCTYPE html>
<html lang="en">
<head>
<meta charset="utf-8">
<title>Alder Croft Transport</title>
<link rel="stylesheet" href="https://fonts.googleapis.com/css2?family=Inter:wght@400;500;600;700&display=swap">
<style>
:root{
  --ruby:#5b222e;
  --ruby-deep:#4d1c27;
  --green:#1f7a5b;
  --green-soft:#3f8f73;
  --band:#2f7e65;
  --mint:#66c1a3;
  --cream:#f6f4f1;
  --tan:#dcc7b0;
  --ink:#1c1c1c;
  --white:#ffffff;
}
*{margin:0;padding:0;box-sizing:border-box}
html,body{width:1200px;height:5155px;overflow:hidden}
body{font-family:"Inter",sans-serif;color:var(--ink);background:var(--cream);position:relative}
.abs{position:absolute}
.photo{position:absolute}
.brand{display:flex;align-items:center;gap:16px;color:var(--white);font-weight:700;letter-spacing:4px;line-height:1}
.brand-mark{width:44px;height:44px;background:var(--white)}
.brand-name{font-size:30px;text-transform:uppercase}
.brand-name span{display:block}

/* hero */
.hero{left:0;top:0;width:1200px;height:808px;background:var(--ruby)}
.hero .brand{position:absolute;left:394px;top:22px}
.hero-title{left:88px;top:314px;width:520px;font-size:48px;font-weight:500;color:var(--white);line-height:56px}
.hero-text{left:88px;top:442px;width:480px;font-size:16px;color:var(--white);line-height:26px}
.btn{display:inline-block;background:var(--mint);color:var(--ruby-deep);font-size:13px;font-weight:500;border-radius:4px;text-align:center}
.hero .btn{position:absolute;left:88px;top:514px;width:114px;height:36px;line-height:36px}

/* partners */
.partners{left:0;top:808px;width:1200px;height:380px;background:var(--cream)}
.partners h2{position:absolute;top:56px;width:100%;text-align:center;font-size:31px;font-weight:500}
.partners-text{position:absolute;top:106px;left:370px;width:460px;text-align:center;font-size:12px;line-height:20px;color:#444}
.partner-row{position:absolute;top:172px;left:0;width:1200px;display:flex;gap:56px;justify-content:center;align-items:center}
.partner{display:flex;align-items:center;gap:10px;font-size:28px;font-weight:700;color:#111}
.partner i{width:34px;height:34px;background:#111;border-radius:50%}

/* feature band */
.band-text{left:0;top:1316px;width:1200px;text-align:center;color:var(--white)}
.band-text h2{font-size:47px;font-weight:500;line-height:56px}
.band-text p{font-size:16px;line-height:26px;margin:22px auto 0;width:520px}

/* services */
.services-title{left:88px;top:1752px;font-size:31px;font-weight:500;color:var(--white)}
.service{position:absolute;width:322px;color:var(--white)}
.service .photo{position:relative;width:322px;height:322px}
.service h3{margin-top:22px;font-size:20px;font-weight:500}

/* testimonial */
.avatar{left:88px;top:2840px;width:66px;height:66px;border-radius:50%;background:#d9d2cc}
.quote{left:88px;top:2918px;width:720px;font-size:20px;line-height:28px;font-weight:500;color:var(--white)}
.quote-by{left:88px;top:3014px;font-size:15px;color:var(--white)}

/* pricing */
.pricing-title{left:0;top:3178px;width:1200px;text-align:center;font-size:31px;font-weight:500;color:var(--white)}
.plan{position:absolute;border:1.5px solid rgba(255,255,255,.55);border-radius:4px;padding:18px 16px;color:var(--white)}
.plan.popular{border-color:var(--white);background:var(--green-soft)}
.tag{display:inline-block;background:var(--white);color:var(--green);font-size:10px;padding:2px 10px;border-radius:10px;margin-bottom:8px}
.plan h4{font-size:15px;font-weight:500}
.price{font-size:34px;font-weight:500;margin-top:18px;line-height:40px}
.per{font-size:12px}
.plan .more{display:block;margin-top:20px;background:var(--tan);color:#333;font-size:10px;text-align:center;height:24px;line-height:24px;border-radius:3px}
.plan .desc{font-size:12px;line-height:19px;margin-top:18px}
.plan ul{list-style:none;margin-top:18px;font-size:12px}
.plan li{display:flex;align-items:center;gap:10px;margin-bottom:10px}

/* faq */
.faq-title{left:88px;top:3802px;font-size:31px;font-weight:500}
.faq{left:88px;top:3868px;width:1024px}
.faq-item{height:83px;display:flex;align-items:center;justify-content:space-between;border-bottom:1px solid #dedad5;font-size:19px;font-weight:500}
.faq-item:last-child{border-bottom:none}

/* map + location */
.map{left:0;top:4392px;width:1200px;height:294px;background:linear-gradient(180deg,#f2f2f0,#e9e9e6)}
.location{left:702px;top:4452px;width:410px;height:108px;background:var(--ruby);border-radius:4px;padding:26px 28px;color:var(--white)}
.location h3{font-size:21px;font-weight:500}
.location p{font-size:12px;margin-top:8px}

/* contact */
.contact{left:0;top:4686px;width:1200px;height:324px;background:var(--ruby);color:var(--white)}
.field-label{position:absolute;font-size:11px}
.field{position:absolute;background:rgba(255,255,255,.12);border-radius:3px}
.contact-legal{position:absolute;left:88px;top:240px;width:290px;font-size:8px;line-height:11px}
.contact-send{position:absolute;left:474px;top:238px;width:98px;height:26px;line-height:26px;font-size:11px}
.contact-title{position:absolute;left:627px;top:66px;font-size:21px;font-weight:500}
.contact-text{position:absolute;left:627px;top:106px;width:480px;font-size:12px;line-height:19px}

/* footer */
.footer{left:0;top:5010px;width:1200px;height:145px;background:var(--green)}
.footer .brand{position:absolute;left:444px;top:44px}
</style>
</head>
<body>

<section class="abs hero">
  <div class="brand"><i class="brand-mark"></i><div class="brand-name"><span>Alder Croft</span><span>Transport</span></div></div>
  <h1 class="abs hero-title">Experience Seamless Transport Solutions</h1>
  <p class="abs hero-text">Our reliable transport services in U.S.A ensure timely and safe deliveries. Trust us for all your transport needs.</p>
  <a class="btn">Learn More</a>
  <div class="photo" role="img" aria-label="Two articulated lorries on a highway under a blue sky" style="left:624px;top:188px;width:492px;height:492px;background:linear-gradient(180deg,#5b8fd6 0%,#b9cde6 40%,#7f8f6a 70%,#6f6a66 100%)"></div>
</section>

<section class="abs partners">
  <h2>Trusted by Leading Companies</h2>
  <p class="partners-text">Our transport services are used by businesses across various sectors in VIC, Australia.</p>
  <div class="partner-row">
    <div class="partner"><i></i>Kestrel</div>
    <div class="partner"><i></i>Northgate</div>
    <div class="partner">Brightway</div>
    <div class="partner"><i></i>Harbourline</div>
    <div class="partner">Fieldmark</div>
  </div>
</section>

<svg class="abs" style="left:0;top:1110px" width="1200" height="1660" viewBox="0 0 1200 1660">
  <polygon points="0,1660 0,500 1200,480 1200,1660" fill="var(--ruby)"/>
  <polygon points="0,70 400,5 1200,70 1200,540 600,600 0,580" fill="var(--band)" role="img" aria-label="Traveller seated inside a bus, tinted green"/>
</svg>
<div class="abs band-text">
  <h2>Choose Reliable<br>Transport</h2>
  <p>We offer prompt and dependable transport services across U.S.A Travel with confidence knowing you are in good hands.</p>
</div>

<h2 class="abs services-title">Our services</h2>
<div class="service" style="left:88px;top:1812px"><div class="photo" role="img" aria-label="Aerial view of a container port" style="background:linear-gradient(160deg,#9fb0b8,#7d6f63 50%,#5e6f6e)"></div><h3>Local Transport Solutions</h3></div>
<div class="service" style="left:438px;top:1812px"><div class="photo" role="img" aria-label="Top view of a cargo ship on green water" style="background:linear-gradient(90deg,#1f4e4a,#4c7f8a 50%,#1f4e4a)"></div><h3>Interstate Transport Services</h3></div>
<div class="service" style="left:788px;top:1812px"><div class="photo" role="img" aria-label="Top view of a cargo ship on green water" style="background:linear-gradient(90deg,#1f4e4a,#4c7f8a 50%,#1f4e4a)"></div><h3>Express Delivery Options</h3></div>
<div class="service" style="left:88px;top:2232px"><div class="photo" role="img" aria-label="Interior of a bus with red seats" style="background:linear-gradient(160deg,#8d7a5e,#b8573f 60%,#5e3a2c)"></div><h3>Freight Management</h3></div>
<div class="service" style="left:438px;top:2232px"><div class="photo" role="img" aria-label="Container ship at sea" style="background:linear-gradient(180deg,#a9b7c6,#8b9bb0 45%,#1d4f96 70%,#1c3f73)"></div><h3>Warehousing Solutions</h3></div>
<div class="service" style="left:788px;top:2232px"><div class="photo" role="img" aria-label="Aerial view of trucks at a loading yard" style="background:linear-gradient(160deg,#6e7378,#a9aaa8 55%,#5a5f63)"></div><h3>Logistics Consulting</h3></div>

<svg class="abs" style="left:0;top:2680px" width="1200" height="1040" aria-hidden="true">
  <polygon points="0,80 1200,0 1200,965 0,1035" fill="var(--green)"/>
</svg>
<div class="abs avatar" role="img" aria-label="Customer portrait"></div>
<p class="abs quote">Alder Croft Transport is fantastic! Their service is reliable and efficient. The team is professional and friendly. Highly recommend for all your transport needs. Thank you!</p>
<p class="abs quote-by">- Maren</p>

<h2 class="abs pricing-title">Pricing</h2>
<div class="plan" style="left:88px;top:3258px;width:342px;height:318px">
  <h4>Basic Transport Service</h4>
  <div class="price">$100</div><div class="per">per job</div>
  <span class="more">More Info</span>
  <p class="desc">Includes local transport within VIC, ensuring safe and timely arrival of goods.</p>
  <ul><li><svg width="10" height="8"><path d="M1 4l3 3 5-6" stroke="#fff" fill="none"/></svg>Local</li><li><svg width="10" height="8"><path d="M1 4l3 3 5-6" stroke="#fff" fill="none"/></svg>Safe</li></ul>
</div>
<div class="plan popular" style="left:428px;top:3246px;width:342px;height:342px">
  <span class="tag">Popular</span>
  <h4>Standard Transport Service</h4>
  <div class="price">$200</div><div class="per">per job</div>
  <span class="more">More Info</span>
  <p class="desc">Covers regional transport across VIC, adding insurance for peace of mind.</p>
  <ul><li><svg width="10" height="8"><path d="M1 4l3 3 5-6" stroke="#fff" fill="none"/></svg>Regional</li><li><svg width="10" height="8"><path d="M1 4l3 3 5-6" stroke="#fff" fill="none"/></svg>Insured</li></ul>
</div>
<div class="plan" style="left:770px;top:3258px;width:342px;height:318px">
  <h4>Premium Transport Service</h4>
  <div class="price">$300</div><div class="per">per job</div>
  <span class="more">More Info</span>
  <p class="desc">Offers statewide transport in VIC, with expedited delivery and priority support.</p>
  <ul><li><svg width="10" height="8"><path d="M1 4l3 3 5-6" stroke="#fff" fill="none"/></svg>Statewide</li><li><svg width="10" height="8"><path d="M1 4l3 3 5-6" stroke="#fff" fill="none"/></svg>Expedited</li></ul>
</div>

<h2 class="abs faq-title">FAQ</h2>
<div class="abs faq">
  <div class="faq-item">What areas do you serve?<svg width="12" height="8"><path d="M1 1l5 5 5-5" stroke="#333" fill="none"/></svg></div>
  <div class="faq-item">What types of transport do you offer?<svg width="12" height="8"><path d="M1 1l5 5 5-5" stroke="#333" fill="none"/></svg></div>
  <div class="faq-item">How can I book a service?<svg width="12" height="8"><path d="M1 1l5 5 5-5" stroke="#333" fill="none"/></svg></div>
  <div class="faq-item">Are your drivers qualified?<svg width="12" height="8"><path d="M1 1l5 5 5-5" stroke="#333" fill="none"/></svg></div>
  <div class="faq-item">Do you offer insurance for transported goods?<svg width="12" height="8"><path d="M1 1l5 5 5-5" stroke="#333" fill="none"/></svg></div>
  <div class="faq-item">What are your operating hours?<svg width="12" height="8"><path d="M1 1l5 5 5-5" stroke="#333" fill="none"/></svg></div>
</div>

<div class="abs map" role="img" aria-label="Street map showing the company location"></div>
<div class="abs location"><h3>Location</h3><p>United States</p></div>

<section class="abs contact">
  <span class="field-label" style="left:88px;top:56px">Name</span>
  <span class="field" style="left:88px;top:72px;width:236px;height:26px"></span>
  <span class="field-label" style="left:336px;top:56px">Email</span>
  <span class="field" style="left:336px;top:72px;width:236px;height:26px"></span>
  <span class="field-label" style="left:88px;top:114px">Message</span>
  <span class="field" style="left:88px;top:130px;width:484px;height:90px"></span>
  <p class="contact-legal">This form is protected by spam checks and our Privacy Policy and Terms of Service apply.</p>
  <a class="btn contact-send">Send</a>
  <h3 class="contact-title">Contact Our Team</h3>
  <p class="contact-text">Reach out to us using the contact form. We are here to assist you with your transport needs in U.S.A</p>
</section>

<footer class="abs footer">
  <div class="brand"><i class="brand-mark"></i><div class="brand-name"><span>Alder Croft</span><span>Transport</span></div></div>
</footer>

</body>
</html>
```